Web Design / Transformation our Joomla web site

Job Type
We are looking for a fresh eye-catching Custom Joomla Design to transform our Joomla web site

Task Description
We are in a process to create web site to Speech Pathology services . The site is built by using brightframe ((http://www.brightframe-example.com/) meadow template.

You can see our site http://littlelanternspeech-example.com/demo

Unfortunately, this template does not match our identity. We would like to improve or replace it. Although we like features that brightframe template is giving as part of their template ,we want to transform our site to something more simplistic and kids oriented . We don’t like look and fill of our website since it’s very professional and “corporate” . Our business is very small and is not 100 people company , we are looking for something more simple and personal. It should look professional, all be it, child friendly. We work on children’s communication skills, and we want to convey an idea that communication is “Little Lantern”, meaning children need to learn to play and socialize appropriately. In addition, learning to be a better communicators will help them to be closer to their family members and friends. We want our website to show kids playing and having fun. In other hand , we don't want the Website to be too busy with images, so use your professional judgment.
You can change current template or you can provide your own Joomla design.

Examples of website look that we like :

http://tinytalkerhub-example.com
http://chattergardenpals-example.com/
http://wrenvoicelessons-example.com/

About Our Company :
Company name: Little Lantern
What we do: Pediatric Speech & Language Pathology Services. We established Little Lantern to provide families with a unique option for their child’s speech therapy needs. Our clinic is founded on the principle that all children are different and require a thoughtful, parent-driven therapy plan. When a family chooses us, they will enter a partnership with an experienced, well-trained therapist.
Top Three Things to Communicate through our Website:
#1 - We are kids friendly
#2 - We are professional
#3 - We provide our services with a loving, nurturing attitude toward the child and with compassionate, comprehensive support and input for the family
Updates

To see current running site : http://littlelanternspeech-example.com/demo/

Reason: There are no good designs to address our needs

Reason: It's still work in progress. Submitted designs are still under constructions and waiting for updates

We are accepting WordPress designs as well !!!

Target Market(s)

Families with kids

Industry/Entity Type

Communication

Requirements
Must have
• • Joomla/Wordpress as a platform
• Easy to Navigate
• Clean Design, kids friendly but professional

```html
<!DOCTYPE html>
<html lang="en">
<head>
<meta charset="utf-8">
<title>Little Lantern – Speech Therapy</title>
<link rel="stylesheet" href="https://fonts.googleapis.com/css2?family=Ubuntu:wght@400;500&family=Open+Sans:wght@400;600;700&family=Noto+Serif:wght@700&family=Cabin+Sketch:wght@400&display=swap">
<style>
:root{
  --dark:#1f1f1f;
  --dark-2:#2b2b2b;
  --board:#1e6a5a;
  --frame:#c8904a;
  --wood:#7a5030;
  --wood-2:#a06a40;
  --accent:#2aa6d6;
  --green:#8cb84a;
  --teal:#2aa9c4;
  --text:#333;
  --muted:#777;
  --line:#e3e3e3;
  --page:#f3f3f3;
  --white:#fff;
}
*{margin:0;padding:0;box-sizing:border-box}
html,body{width:1200px;height:2621px;overflow:hidden}
body{position:relative;background:var(--page);font-family:"Open Sans",sans-serif;color:var(--text)}
.abs{position:absolute}

/* header */
.topbar{left:0;top:0;width:1200px;height:96px;background:var(--dark)}
.logo{left:180px;top:6px;font-family:"Ubuntu",sans-serif;font-weight:500;font-size:30px;color:var(--white);letter-spacing:1px}
.search{left:825px;top:12px;width:195px;height:26px;display:flex}
.search span{flex:1;background:#fff;font-size:11px;color:#999;padding:6px 8px}
.search i{width:26px;background:var(--accent)}
.nav{left:180px;top:64px;display:flex;gap:26px;font-family:"Ubuntu",sans-serif;font-size:12.5px;color:#ccc;letter-spacing:.5px}
.nav .on{color:#fff}
.hero{left:0;top:96px;width:1200px;height:384px;background:radial-gradient(ellipse at 40% 40%,#3a3a3a,#181818)}
.board{left:183px;top:148px;width:327px;height:246px;border:12px solid var(--frame);background:var(--board);border-radius:4px;box-shadow:0 6px 14px rgba(0,0,0,.5)}
.board h2{font-family:"Cabin Sketch",sans-serif;font-weight:400;font-size:104px;color:#e8f4ee;text-align:center;line-height:1;margin-top:14px}
.board p{color:#fff;font-size:14px;line-height:1.5;padding:10px 22px 0}
.person{left:660px;top:110px;width:320px;height:370px;background:linear-gradient(180deg,#caa070,#eee 55%,#333);border-radius:160px 160px 0 0}

/* category bar */
.catbar{left:190px;top:510px;width:815px;height:115px;background:linear-gradient(180deg,var(--wood-2),var(--wood));border-radius:4px;box-shadow:0 4px 8px rgba(0,0,0,.3)}
.catbar .inner{position:absolute;left:14px;top:14px;right:14px;bottom:14px;background:#222;display:flex;align-items:center;padding:0 30px;gap:50px}
.catbar h3{font-family:"Noto Serif",serif;font-style:italic;font-weight:700;font-size:16px;color:#eee;width:150px}
.select{width:170px;height:26px;background:#3a3a3a;color:#999;font-size:11px;padding:6px 8px}
.kw{margin-left:40px;width:160px;height:26px;background:#3a3a3a;color:#999;font-size:11px;padding:6px 8px}
.go{width:28px;height:26px;background:var(--accent);margin-left:-50px}

/* posts */
.content{left:180px;top:650px;width:535px;height:1720px;background:var(--white)}
.post{position:absolute;left:18px;width:500px}
.post h2{font-family:"Noto Serif",serif;font-size:17px;line-height:1.3;color:#222}
.post p{font-size:12.5px;line-height:1.6;color:var(--muted);margin-top:10px}
.more{display:inline-block;margin-top:16px;background:var(--accent);color:#fff;font-size:12px;font-weight:600;padding:6px 18px;border-radius:14px}
.sep{position:absolute;left:18px;width:500px;height:1px;background:var(--line)}
.pager{left:440px;top:2318px;display:flex;gap:4px;font-size:11px}
.pager span{min-width:22px;height:22px;border:1px solid #ddd;background:#fff;text-align:center;line-height:20px;color:#555;padding:0 4px}
.pager .cur{background:var(--accent);color:#fff;border-color:var(--accent)}

/* sidebar */
.side{left:735px;width:285px;background:var(--white)}
.stats{top:650px;height:80px;display:flex}
.stats div{flex:1;text-align:center;padding-top:30px;border:1px solid var(--line)}
.stats b{display:block;font-size:20px;color:var(--teal)}
.stats small{font-size:9px;color:var(--muted)}
.subs{top:745px;height:35px;display:flex;gap:6px;background:none}
.subs span{flex:1;border:1px solid var(--line);background:#fff;font-size:10.5px;padding:9px 8px;color:#444}
.email{top:786px;height:28px;display:flex;gap:8px;background:none;padding-left:10px}
.email span{width:150px;border:1px solid #ccc;background:#fff;font-size:10px;color:#999;padding:6px}
.email b{width:80px;background:var(--teal);color:#fff;font-size:11px;font-weight:600;text-align:center;line-height:28px}
.tabs{top:843px;height:26px;display:flex;font-size:10.5px;background:#f7f7f7;border:1px solid var(--line)}
.tabs span{padding:5px 10px;border-right:1px solid var(--line)}
.fb{top:872px;height:240px;border:1px solid #c5cde0;padding:8px}
.fb .head{font-size:9px;font-weight:700;color:#3b5998}
.fb .row{display:flex;align-items:center;gap:10px;margin-top:14px}
.fb .sq{width:36px;height:36px;background:var(--teal);color:#fff;font-weight:700;text-align:center;line-height:36px}
.fb .btn{font-size:9px;border:1px solid #ccc;padding:2px 6px}
.fb small{display:block;font-size:9px;color:#555;margin-top:8px}
.faces{display:grid;grid-template-columns:repeat(6,36px);gap:5px;margin-top:8px}
.faces i{height:36px;background:linear-gradient(135deg,#b8a08a,#6b7a8c)}
.recent{top:1135px;height:320px}
.recent h4{background:var(--green);color:#fff;font-size:14px;font-weight:600;padding:8px 10px}
.recent ol{list-style:none}
.recent li{display:flex;gap:10px;padding:6px 10px;border-bottom:1px solid var(--line);height:45px;align-items:flex-start}
.recent li b{font-family:"Ubuntu",sans-serif;font-weight:400;font-size:24px;color:var(--teal);line-height:1;width:32px}
.recent li span{font-family:"Noto Serif",serif;font-weight:700;font-size:11px;line-height:1.35;color:#333}

/* footer */
.footer{left:0;top:2395px;width:1200px;height:226px;background:#ececec;border-top:1px solid #ddd}
.flinks{left:180px;top:2473px;display:flex;gap:58px;font-size:11px;color:var(--muted)}
.copy{left:180px;top:2535px;font-size:10.5px;color:var(--muted)}
</style>
</head>
<body>
<div class="abs topbar"></div>
<div class="abs logo">Speech Logo</div>
<div class="abs search"><span>Search ...</span><i></i></div>
<nav class="abs nav">
  <span class="on">HOME</span><span>ABOUT ME</span><span>FREE WORKSHEETS</span><span>LINKS</span><span>PLEASE READ</span><span>SPEECH THERAPY</span><span>STORE</span><span>LANTERNPLAY</span>
</nav>

<div class="abs hero"></div>
<div class="abs board">
  <h2>404</h2>
  <p>Lorem Ipsum is simply dummy text of the printing and typesetting industry. Lorem Ipsum has been the industry's standard</p>
</div>
<div class="abs person" role="img" aria-label="Photo of a thoughtful young woman holding a book, with chalk doodles"></div>

<div class="abs catbar"><div class="inner">
  <h3>Select Categories</h3>
  <div class="select">Categories</div>
  <div class="kw">Type your keyword</div>
  <div class="go"></div>
</div></div>

<main class="abs content">
  <article class="post" style="top:22px">
    <h2>Lorem Ipsum is simply dummy text of the printing and typesetting industry.</h2>
    <p>We've talked a lot about helping kids with articulation disorders here on Tiny Talker Hub. I've shared my Articulation Screener to help you identify the sounds kids are saying in error as well as an Articulation Goal Tracker to help select the sounds</p>
    <span class="more">Read More</span>
  </article>
  <div class="sep" style="top:258px"></div>
  <article class="post" style="top:292px">
    <h2>Lorem Ipsum is simply dummy text of the printing and typesetting industry.</h2>
    <p>Teaching the R Sound can be very challenging. Learning new ways to make teaching this sound easier fascinates me. I'd like to thank Milo Brandt from Clearword Labs for taking the time to share with us</p>
    <span class="more" style="margin-top:44px">Read More</span>
  </article>
  <div class="sep" style="top:540px"></div>
  <article class="post" style="top:578px">
    <h2>Lorem Ipsum is simply dummy text of the printing and typesetting industry.</h2>
    <p>No more waiting! You can now download articulation practice worksheets for the following sounds: /b/, /h/, /w/, /f/, /v/, /n/, /ng/, /r/ and /s/ These have been added to the Worksheets page along with all the other available sounds!</p>
    <span class="more">Read More</span>
  </article>
  <div class="sep" style="top:830px"></div>
  <article class="post" style="top:868px">
    <h2>Lorem Ipsum is simply dummy text of the printing and typesetting industry.</h2>
    <p>Did you know that May is Better Hearing and Speech Month? What is Better Hearing and Speech month all about? I believe NVHA (National Voice-Hearing Language-Hearing</p>
    <span class="more">Read More</span>
  </article>
  <div class="sep" style="top:1115px"></div>
  <article class="post" style="top:1155px">
    <h2>Lorem Ipsum is simply dummy text of the printing and typesetting industry.</h2>
    <p>My little Junie is two months old now. Last night she finally slept for long enough that this morning I feel half way normal. Yay! I decided to sit down and write a post to celebrate a clear mind</p>
    <span class="more">Read More</span>
  </article>
  <div class="sep" style="top:1400px"></div>
  <article class="post" style="top:1440px">
    <h2>Lorem Ipsum is simply dummy text of the printing and typesetting industry.</h2>
    <p>I have found that the most difficult thing for a lot of parents to do when trying to correct their children's speech errors on their own is to teach that initial correct production of a sound.</p>
    <span class="more">Read More</span>
  </article>
</main>
<div class="abs pager"><span class="cur">1</span><span>2</span><span>3</span><span>4</span><span>5</span><span>6</span><span>7</span><span>8</span><span>...</span><span>Last »</span></div>

<aside>
  <div class="abs side stats">
    <div><b>57,886</b><small>Chirper Followers</small></div>
    <div><b>131,685</b><small>Friendbook Fans</small></div>
  </div>
  <div class="abs side subs"><span>Get Email Updates</span><span>Subscribe via RSS</span></div>
  <div class="abs side email"><span>me@email.com</span><b>Subscribe</b></div>
  <div class="abs side tabs"><span>Friendbook</span><span>Chirper</span><span>Circles+</span></div>
  <div class="abs side fb">
    <div class="head">Find us on Friendbook</div>
    <div class="row"><div class="sq">L</div><span class="btn">Like</span></div>
    <small>22,483 people like this.</small>
    <div class="faces" role="img" aria-label="Grid of small fan profile photos"><i></i><i></i><i></i><i></i><i></i><i></i><i></i><i></i><i></i><i></i><i></i><i></i></div>
    <small>Friendbook social plugin</small>
  </div>
  <div class="abs side recent">
    <h4>Recent Posts</h4>
    <ol>
      <li><b>01</b><span>Lorem Ipsum is simply dummy text of the printing.</span></li>
      <li><b>02</b><span>Lorem Ipsum is simply dummy text of the printing.</span></li>
      <li><b>03</b><span>Lorem Ipsum is simply dummy text of the printing.</span></li>
      <li><b>04</b><span>Lorem Ipsum is simply dummy text of the printing.</span></li>
      <li><b>05</b><span>Lorem Ipsum is simply dummy text of the printing and typesetting industry.</span></li>
      <li><b>06</b><span>Lorem Ipsum is simply dummy text of the printing.</span></li>
    </ol>
  </div>
</aside>

<footer class="abs footer"></footer>
<div class="abs flinks"><span>Advertise</span><span>Suggestions</span><span>About Us</span><span>Terms and Conditions</span><span>Privacy Policy Write for Us</span></div>
<div class="abs copy">Copyright © 2013 Little Lantern</div>
</body>
</html>
```